Letterhead for Business Law Firm

We need a letter head for our firm based on the design we have settled on and it is attached. Our clients are small and large businesses around the world, and our letterhead is used typically for formal legal purposes such as demand letters (accusing the recipient of doing bad things) or responding to demand letters. It may also be sent to regulators and other government agencies. So this needs to be tasteful, but a little edgy as well - we try to convey that we are a firm that is different - businesses and investors come to us for creative, quick advice, typically in high stress circumstances, and for our ability to work through high conflict situations, and rapid paced engagements.

Target Market(s)

Lawyers, business executives, investors, government regulators who may receive letters from this firm on behalf of its clients.

Industry/Entity Type

Business

Requirements
Must have
• The design and the firm's contact information:
• Thornvale Law Firm, P.C.
• 8172 SW 17th Ave
• Portland, OR 97058
• phone: 971 555 0147
• fax: 971 555 0182
• in what placement and how depicted (e.g. a phone icon instead of the word "phone") I leave to your creative ideas.
Nice to have
• design and information can be placed at the top, bottom and/or sides of the letter, and the design should be for a standard letter size paper - and can have a separate design for the second page.

```html
<!DOCTYPE html>
<html lang="en">
<head>
<meta charset="utf-8">
<title>Thornvale Law Firm, P.C. — Letterhead</title>
<link rel="stylesheet" href="https://fonts.googleapis.com/css2?family=Josefin+Sans:wght@300;400&family=Arimo:wght@400&display=swap">
<style>
  :root {
    --backdrop: #e6e6e8;
    --paper: #ffffff;
    --ink-dark: #231f20;
    --teal: #2f6675;
    --teal-light: #6fa3b1;
    --rule: #5d8794;
    --footer-text: #e9eef0;
  }
  * { box-sizing: border-box; margin: 0; padding: 0; }
  html, body {
    width: 1200px; height: 848px; overflow: hidden;
    background: var(--backdrop);
  }
  .canvas { position: relative; width: 1200px; height: 848px; }
  .letterhead {
    position: absolute; left: 290px; top: 24px;
    width: 620px; height: 800px;
    background: var(--paper);
    box-shadow: 0 2px 10px rgba(0,0,0,0.12);
  }
  .letterhead__brand {
    position: absolute; right: 44px; top: 20px;
    display: flex; align-items: center; gap: 10px;
  }
  .brand-square { width: 22px; height: 22px; background: var(--teal); }
  .brand-name {
    font-family: 'Josefin Sans', sans-serif;
    font-weight: 300; font-size: 26px; letter-spacing: 9px;
    color: var(--ink-dark); line-height: 1;
  }
  .letterhead__rule {
    position: absolute; left: 0; right: 0; top: 58px;
    height: 1px; background: var(--rule);
  }
  .footer { position: absolute; left: 0; right: 0; bottom: 0; }
  .footer__address {
    height: 16px; background: var(--teal);
    display: flex; align-items: center; gap: 8px;
    padding-left: 10px;
    font-family: 'Arimo', sans-serif; font-size: 8px;
    color: var(--footer-text); letter-spacing: 0.3px;
    white-space: nowrap;
  }
  .footer__address .sep { opacity: 0.7; }
  .footer__address svg { width: 10px; height: 8px; }
  .footer__band { position: relative; height: 40px; background: var(--ink-dark); }
  .footer__keys {
    position: absolute; left: 0; right: 0; top: 0; height: 12px;
    background: linear-gradient(90deg, #e9eef0 0%, var(--teal-light) 50%, #e9eef0 100%);
    opacity: 0.85;
  }
  .footer__contacts {
    position: absolute; left: 0; right: 0; bottom: 6px;
    display: flex; justify-content: flex-end; gap: 26px;
    padding-right: 14px;
    font-family: 'Arimo', sans-serif; font-size: 8px;
    color: var(--footer-text); letter-spacing: 0.3px;
    white-space: nowrap;
  }
  .contact { display: flex; align-items: center; gap: 5px; }
  .contact svg { width: 10px; height: 10px; }
</style>
</head>
<body>
<main class="canvas">
  <article class="letterhead">
    <header class="letterhead__brand">
      <span class="brand-square"></span>
      <span class="brand-name">THORNVALE</span>
    </header>
    <div class="letterhead__rule"></div>

    <footer class="footer">
      <div class="footer__address">
        <span>Thornvale Law Firm, P.C.</span><span class="sep">|</span>
        <span>8172 SW 17th Ave</span><span class="sep">|</span>
        <span>P.O. Box 40518</span><span class="sep">|</span>
        <span>Portland, OR 97058</span>
        <svg viewBox="0 0 10 8" aria-hidden="true"><rect x="0.5" y="0.5" width="9" height="7" fill="none" stroke="#e9eef0"/><path d="M0.5 0.5 L5 4.5 L9.5 0.5" fill="none" stroke="#e9eef0"/></svg>
      </div>
      <div class="footer__band">
        <div class="footer__keys" role="img" aria-label="Decorative piano-key stripe pattern in white and teal"></div>
        <div class="footer__contacts">
          <span class="contact">
            <svg viewBox="0 0 10 10" aria-hidden="true"><circle cx="5" cy="5" r="4.3" fill="none" stroke="#e9eef0"/><ellipse cx="5" cy="5" rx="1.8" ry="4.3" fill="none" stroke="#e9eef0"/><line x1="0.7" y1="5" x2="9.3" y2="5" stroke="#e9eef0"/></svg>
            www.thornvalelaw.com
          </span>
          <span class="contact">
            <svg viewBox="0 0 10 10" aria-hidden="true"><rect x="2.5" y="0.5" width="5" height="9" rx="1" fill="none" stroke="#e9eef0"/><line x1="4" y1="8" x2="6" y2="8" stroke="#e9eef0"/></svg>
            971 555 0147
          </span>
          <span class="contact">
            <svg viewBox="0 0 10 10" aria-hidden="true"><rect x="2.5" y="0.5" width="5" height="3" fill="none" stroke="#e9eef0"/><rect x="0.5" y="3.5" width="9" height="4" fill="none" stroke="#e9eef0"/><rect x="2.5" y="6" width="5" height="3.5" fill="none" stroke="#e9eef0"/></svg>
            Fax 971 555 0182
          </span>
          <span class="contact">
            <svg viewBox="0 0 10 10" aria-hidden="true"><rect x="0.5" y="0.5" width="9" height="9" fill="none" stroke="#e9eef0"/><path d="M0.5 2 L5 5.5 L9.5 2" fill="none" stroke="#e9eef0"/></svg>
            office@thornvalelaw.com
          </span>
        </div>
      </div>
    </footer>
  </article>
</main>
</body>
</html>
```